Harborline Bridal Bakery Selling Method needs finishing touches to website.

We have a temporary website located at http://www.brivantomarketworks.com/ql/.
We are doing a responsive design and have created the architecture (layout). However, we need a professional makeover for the graphic elements and colors of the website. The website will be selling a sales course to mostly women who sell wedding cakes.
The photos within the posted website are for illustrative purposes. We will use our own photos after the website is redone.
We are open to changing the font styles, borders, header, and anything else as long as the layout is not changed.
Target Market(s)
75% women age 25-50 and men 30-60.
Industry/Entity Type
Architecture
Colors
Designer to choose colors to be used in the design.
Look and feel
Each slider illustrates characteristics of the customer's brand and the style your logo design should communicate.

```html
<!DOCTYPE html>
<html lang="en">
<head>
<meta charset="utf-8">
<title>Harborline Bridal Bakery Selling Method</title>
<link rel="stylesheet" href="https://fonts.googleapis.com/css2?family=Tinos:wght@400;700&family=Arimo:wght@400;700&display=swap">
<style>
  :root {
    --mauve: #a85e71;
    --mauve-dark: #8f4a5c;
    --plum: #8e1f6e;
    --hot-pink: #ff0066;
    --ink: #222222;
    --grey-band: #ededed;
    --grey-text: #777777;
    --header-bg: #f2f2f2;
    --white: #ffffff;
    --black-btn: #1f1f1f;
  }
  * { box-sizing: border-box; margin: 0; padding: 0; }
  html, body { width: 774px; height: 1200px; overflow: hidden; background: var(--white); }
  body { position: relative; font-family: "Arimo", Arial, sans-serif; color: var(--ink); }
  .abs { position: absolute; }

  /* Header */
  .site-header { left: 0; top: 0; width: 774px; height: 76px; background: var(--header-bg); }
  .brand { left: 33px; top: 16px; width: 170px; font-family: "Tinos", "Times New Roman", serif; font-weight: 700; font-size: 19px; line-height: 22px; color: var(--ink); }
  .member-login { left: 273px; top: 26px; display: flex; align-items: center; gap: 5px; font-family: "Tinos", serif; font-size: 13px; color: #555; }
  .signup-btn { background: #333; color: var(--white); font-family: "Arimo", sans-serif; font-size: 13px; padding: 2px 8px; border-radius: 3px; margin-left: 3px; }
  .search-box { left: 528px; top: 27px; width: 233px; height: 21px; background: var(--white); border: 1px solid #ddd; font-size: 11px; color: #999; padding: 3px 6px; }
  .search-box svg { position: absolute; right: 6px; top: 3px; }

  /* Hero */
  .hero-photo { left: 0; top: 76px; width: 519px; height: 194px; background: linear-gradient(135deg, #cfc3bd 0%, #e9dfd8 35%, #f3e6e6 60%, #d9c9c8 100%); }
  .hero-title { left: 22px; top: 94px; font-family: "Tinos", serif; font-weight: 700; font-size: 38px; line-height: 44px; color: var(--white); text-shadow: 1px 2px 2px rgba(0,0,0,.55); letter-spacing: -0.5px; }
  .hero-sub { left: 34px; top: 140px; width: 230px; font-family: "Tinos", serif; font-weight: 700; font-size: 18px; line-height: 18px; color: #e8e8e8; text-shadow: 1px 1px 2px rgba(0,0,0,.7); }
  .hero-cta { left: 24px; top: 215px; width: 368px; height: 45px; background: var(--mauve); border-radius: 10px; color: var(--white); font-family: "Tinos", serif; font-weight: 700; font-size: 21px; line-height: 45px; text-align: center; }

  /* Join form */
  .join-panel { left: 519px; top: 76px; width: 253px; height: 293px; background: var(--mauve); box-shadow: 0 2px 6px rgba(0,0,0,.45); }
  .join-title { position: absolute; left: 75px; top: 8px; width: 100px; height: 31px; background: var(--black-btn); color: var(--white); font-weight: 700; font-size: 12px; line-height: 31px; text-align: center; border-radius: 4px; box-shadow: 0 1px 3px rgba(0,0,0,.5); }
  .field { position: absolute; left: 9px; width: 233px; }
  .field label { display: block; color: var(--white); font-weight: 700; font-size: 9px; height: 11px; }
  .field span { display: block; height: 23px; background: var(--white); border-radius: 3px; border: 1px solid #d9b9c1; }
  .submit-btn { position: absolute; left: 139px; top: 255px; width: 103px; height: 26px; background: var(--black-btn); color: var(--white); font-weight: 700; font-size: 13px; line-height: 26px; text-align: center; border-radius: 4px; }

  /* Section bars */
  .section-bar { background: var(--mauve); color: var(--white); text-align: center; border-radius: 4px; box-shadow: 0 1px 2px rgba(0,0,0,.2); font-weight: 400; }
  .featured-bar { left: 17px; top: 290px; width: 496px; height: 52px; font-family: "Tinos", serif; font-size: 24px; line-height: 52px; }
  .marketing-bar { left: 160px; top: 795px; width: 482px; height: 46px; font-size: 25px; line-height: 46px; }

  /* Services */
  .service { left: 33px; width: 650px; height: 118px; }
  .service-photo { position: absolute; left: 0; top: 0; width: 145px; height: 118px; border: 2px solid #888; }
  .service-body { position: absolute; left: 184px; top: 2px; width: 440px; }
  .service-body h3 { font-size: 19px; font-weight: 700; color: var(--plum); margin-bottom: 8px; }
  .service-body p { font-size: 8.5px; line-height: 11px; color: #333; }
  .service-body .more { color: var(--plum); font-weight: 700; }
  .service-body .note { margin-top: 24px; }
  .service-body .note b { color: var(--plum); }

  .marketing-intro { left: 18px; top: 864px; width: 738px; font-size: 9px; line-height: 13px; text-align: center; color: #333; }

  /* Cards */
  .card { top: 904px; width: 237px; height: 180px; background: var(--hot-pink); }
  .card-photo { position: absolute; left: 65px; top: 0; width: 172px; height: 150px; }
  .card-label { position: absolute; right: 10px; bottom: 6px; color: var(--white); font-weight: 700; font-size: 16px; }

  /* Newsletter + footer */
  .newsletter { left: 0; top: 1104px; width: 774px; height: 66px; background: var(--grey-band); }
  .newsletter p { position: absolute; left: 29px; top: 27px; font-size: 13px; color: var(--grey-text); }
  .subscribe-btn { position: absolute; left: 572px; top: 18px; width: 189px; height: 30px; background: var(--mauve); color: var(--white); font-weight: 700; font-size: 13px; letter-spacing: 1px; line-height: 30px; text-align: center; }
  .site-footer { left: 0; top: 1188px; width: 774px; height: 12px; background: var(--mauve-dark); color: var(--white); font-size: 8px; font-weight: 700; line-height: 12px; text-align: center; }
</style>
</head>
<body>

<header class="site-header abs">
  <div class="brand abs">Harborline Bridal Bakery</div>
  <div class="member-login abs">
    <svg width="14" height="18" viewBox="0 0 14 18" aria-hidden="true"><path d="M3.5 8V5.5a3.5 3.5 0 0 1 7 0V8" fill="none" stroke="#444" stroke-width="2"/><rect x="1" y="8" width="12" height="9" rx="1.5" fill="#444"/></svg>
    <span>Login MEMBERS AREA</span>
    <span class="signup-btn">Sign Up</span>
  </div>
  <div class="search-box abs">Search..
    <svg width="13" height="13" viewBox="0 0 13 13" aria-hidden="true"><circle cx="5.5" cy="5.5" r="4" fill="none" stroke="#999" stroke-width="1.5"/><path d="M8.5 8.5l3.5 3.5" stroke="#999" stroke-width="1.5"/></svg>
  </div>
</header>

<section class="hero">
  <div class="hero-photo abs" role="img" aria-label="Photo of tiered wedding cakes with pink sugar flowers on a dessert table"></div>
  <h1 class="hero-title abs">Harborline Bridal Bakery</h1>
  <p class="hero-sub abs">Lorem Ipsum is Dummy Text</p>
  <a class="hero-cta abs">Click here to see our services</a>
</section>

<form class="join-panel abs">
  <div class="join-title">JOIN US NOW</div>
  <div class="field" style="top:60px"><label>First Name:</label><span></span></div>
  <div class="field" style="top:99px"><label>Last Name:</label><span></span></div>
  <div class="field" style="top:137px"><label>Email:</label><span></span></div>
  <div class="field" style="top:176px"><label>Address:</label><span></span></div>
  <div class="field" style="top:215px"><label>Phone:</label><span></span></div>
  <div class="submit-btn">SUBMIT</div>
</form>

<h2 class="section-bar featured-bar abs">Our Featured Services</h2>

<article class="service abs" style="top:390px">
  <div class="service-photo" style="background:linear-gradient(160deg,#6b5a52,#e8d6d6 55%,#c9a0aa)" role="img" aria-label="Photo of a white wedding cake with pink trim and a ring topper"></div>
  <div class="service-body">
    <h3>Lorem Ipsum</h3>
    <p>Lorem Ipsum is simply dummy text of the printing and typesetting industry. Lorem Ipsum has been the industry's standard dummy text ever since the 1500s, when an unknown printer took a galley of type and scrambled it to make a type specimen book.<br><span class="more">Click here to learn more.</span></p>
    <p class="note">*Available to <b>BASIC</b> and <b>FULL</b> Members only.</p>
  </div>
</article>

<article class="service abs" style="top:520px">
  <div class="service-photo" style="background:linear-gradient(160deg,#7a4a55,#d9a9b4 50%,#8b5c66)" role="img" aria-label="Photo of rows of pink frosted cupcakes"></div>
  <div class="service-body">
    <h3>Lorem Ipsum</h3>
    <p>Lorem Ipsum is simply dummy text of the printing and typesetting industry. Lorem Ipsum has been the industry's standard dummy text ever since the 1500s, when an unknown printer took a galley of type and scrambled it to make a type specimen book.<br><span class="more">Click here to learn more.</span></p>
    <p class="note">*Available to <b>BASIC</b> and <b>FULL</b> Members only.</p>
  </div>
</article>

<article class="service abs" style="top:641px">
  <div class="service-photo" style="background:linear-gradient(160deg,#3e3a3a,#e9e4e2 55%,#a89a98)" role="img" aria-label="Photo of a couple cutting a tiered wedding cake"></div>
  <div class="service-body">
    <h3>Lorem Ipsum</h3>
    <p>Lorem Ipsum is simply dummy text of the printing and typesetting industry. Lorem Ipsum has been the industry's standard dummy text ever since the 1500s, when an unknown printer took a galley of type and scrambled it to make a type specimen book.<br><span class="more">Click here to learn more.</span></p>
    <p class="note">*Available to <b>BASIC</b> and <b>FULL</b> Members only.</p>
  </div>
</article>

<h2 class="section-bar marketing-bar abs">MARKETING SERVICES</h2>
<p class="marketing-intro abs">No matter the size of your salon, spa or medi-spa, we have marketing solutions, tools and education available for you. To learn more about our suites of various services, click a category below to get started. If you want immediate help, click here to request a marketing specialist to contact you.</p>

<a class="card abs" style="left:11px">
  <div class="card-photo" style="background:linear-gradient(160deg,#f2f2f2,#c9c3bf 55%,#2b2b2b)" role="img" aria-label="Photo of two business people in suits"></div>
  <span class="card-label">Lorem Ipsum</span>
</a>
<a class="card abs" style="left:262px">
  <div class="card-photo" style="background:linear-gradient(160deg,#e6e9ec,#8f9aa3 55%,#3a3f45)" role="img" aria-label="Photo of a businessman at a self-service kiosk"></div>
  <span class="card-label">Lorem Ipsum</span>
</a>
<a class="card abs" style="left:512px">
  <div class="card-photo" style="background:linear-gradient(160deg,#f3ede9,#d8c6bf 50%,#6d5e58)" role="img" aria-label="Photo of colleagues working around a tablet"></div>
  <span class="card-label">Lorem Ipsum</span>
</a>

<section class="newsletter abs">
  <p>Please subscribe to our newsletter to receive all the latest news and events directly</p>
  <a class="subscribe-btn">SUBSCRIBE NOW</a>
</section>

<footer class="site-footer abs">© Copyright, Harborline Bridal Bakery, 48 Lantern Row, Suite 210, Marlow, OR 97310, Tel: 555-014-2290, Email: hello@harborlinebakery.com</footer>

</body>
</html>
```